Meadow Lark Honey and Combs produces and sells local raw honey.

The logo is in the files. Use the one with the brown letters. We are looking to have a web page that tells our customers about our products and where they can be purchased. We may take orders and sell from this web page in the future. We would like to have a way for customers to ask questions or provide feedback. I've provided pictures but it will be up to the designer's discretion to use whatever pictures are relevant to the design.

Target Market(s)

Customers in the greater Seattle area.

Coding

Coded - Design and coding required

Number of Pages Required

3 page

Font styles to use
Sans Serif

Colors

Designer to choose colors to be used in the design.

Requirements
Must have
• A message that we produce and sell only pure raw local honey. Raw honey means it has never been flavored, heated, pasteurized, filtered or has additives of any kind. The web page should also let people know where they can find our honey for purchase.

```html
<!DOCTYPE html>
<html lang="en">
<head>
<meta charset="utf-8">
<title>Meadow Lark Honey</title>
<link rel="stylesheet" href="https://fonts.googleapis.com/css2?family=Jost:wght@400;500;600&family=Italiana&display=swap">
<style>
:root{
  --yellow:#e3df0b;
  --brown:#2b1512;
  --ink:#2e2e2e;
  --grey:#8a8a8a;
  --page:#f2f3f7;
  --footer:#454a54;
  --white:#ffffff;
}
*{box-sizing:border-box;margin:0;padding:0}
html,body{width:1200px;height:2917px;overflow:hidden}
body{position:relative;background:var(--white);font-family:'Jost',sans-serif;color:var(--ink)}
.abs{position:absolute}
.display{font-family:'Italiana',serif;font-style:italic;letter-spacing:2px}
.btn{position:absolute;display:flex;align-items:center;justify-content:center;border-radius:30px;font-size:13px;font-weight:500;color:var(--brown)}
.btn-solid{background:var(--yellow)}
.btn-line{border:2px solid var(--yellow);background:var(--white)}

/* header */
.site-header{left:0;top:0;width:1200px;height:95px;background:var(--white);z-index:3}
.brand-oval{left:150px;top:0;width:225px;height:135px;background:var(--white);border-radius:0 0 50% 50%;z-index:4;display:flex;align-items:center;justify-content:center;gap:8px}
.brand-oval .dot{width:14px;height:14px;border-radius:50%;background:var(--brown)}
.brand-oval span{font-size:19px;font-weight:600;color:var(--brown)}
.nav{left:400px;top:0;height:95px;display:flex;gap:0;font-size:13px;z-index:4}
.nav a{position:relative;display:block;padding:40px 18px 0;color:var(--ink);text-decoration:none}
.nav a.active::before{content:"";position:absolute;left:18px;right:18px;top:0;height:4px;background:var(--yellow)}
.quote-btn{left:846px;top:31px;width:146px;height:38px;z-index:4}
.cart{left:1012px;top:24px;z-index:4}

/* hero */
.hero{left:0;top:95px;width:1200px;height:440px;background:linear-gradient(100deg,#4e3d22 0%,#8c7a48 35%,#6d5a34 60%,#2f2416 100%)}
.hero-title{left:0;top:230px;width:1200px;text-align:center;font-size:42px;color:var(--white)}
.hero-sub{left:0;top:285px;width:1200px;text-align:center;font-size:18px;line-height:24px;color:var(--white)}
.hero-btn{left:528px;top:355px;width:144px;height:38px}

/* intro */
.intro-title{left:156px;top:622px;font-size:32px;color:var(--brown)}
.intro-lead{left:156px;top:672px;width:500px;font-size:15px;line-height:21px;color:var(--grey)}
.intro-text{left:156px;top:758px;width:500px;font-size:12.5px;line-height:18px;color:var(--grey)}
.intro-btn{left:156px;top:853px;width:144px;height:36px}
.intro-art{left:520px;top:560px;width:680px;height:445px;background:radial-gradient(ellipse at 70% 55%,#f0b43a 0%,#e8a02a 30%,rgba(240,200,120,.4) 55%,rgba(255,255,255,0) 72%)}

/* quote band */
.band{left:0;top:1002px;width:1200px;height:392px;background:linear-gradient(90deg,#5a5148 0%,#8a8379 35%,#77716a 70%,#5e5850 100%)}
.band-jars{left:150px;top:1040px;width:380px;height:320px;background:radial-gradient(ellipse at center,#2a1414 0%,#3b201b 55%,rgba(60,40,30,0) 75%)}
.quote-card{left:688px;top:955px;width:358px;height:487px;background:var(--yellow);border-radius:6px;overflow:hidden;box-shadow:0 8px 20px rgba(0,0,0,.25)}
.quote-head{position:absolute;left:0;top:0}
.quote-card h2{position:absolute;left:0;top:22px;width:358px;text-align:center;font-weight:400;font-size:26px;color:var(--white)}
.quote-card .lede{position:absolute;left:40px;top:60px;width:278px;text-align:center;font-size:11px;line-height:15px;color:var(--white)}
.field{position:absolute;left:34px;width:290px;height:33px;background:var(--white);font-size:11px;color:var(--grey);padding:10px 12px}
.send-btn{left:118px;top:403px;width:122px;height:36px;border:2px solid var(--brown);background:transparent;gap:8px}

/* featured */
.featured{left:0;top:1394px;width:1200px;height:613px;background:var(--page)}
.section-title{font-size:30px;color:var(--brown)}
.title-rule{height:2px;width:50px;background:var(--yellow)}
.viewall{width:112px;height:34px}
.product{position:absolute;top:1545px;width:204px;height:398px;background:var(--white);border:1px solid #e3e4e8}
.product.lift{box-shadow:0 8px 18px rgba(0,0,0,.12)}
.product .jar{position:absolute;left:45px;top:28px;width:114px;height:160px;border-radius:10px;background:linear-gradient(180deg,#3a1f1b,#1e0e0c)}
.product.lift .jar{background:linear-gradient(180deg,#9a9593,#7b7674)}
.product .sep{position:absolute;left:16px;right:16px;top:218px;height:1px;background:#e3e4e8}
.product .name{position:absolute;left:0;top:240px;width:204px;text-align:center;font-size:15px;line-height:20px;color:#555}
.product .price{position:absolute;left:0;top:298px;width:204px;text-align:center;font-family:'Italiana',serif;font-style:italic;font-size:21px;color:var(--ink)}
.product .order{left:44px;top:345px;width:116px;height:34px}
.hover-icons{position:absolute;left:47px;top:96px;display:flex;gap:8px}
.hover-icons span{width:30px;height:30px;border-radius:50%;background:var(--brown);display:flex;align-items:center;justify-content:center}
.hover-icons span.on{background:var(--yellow)}
.circle-arrow{position:absolute;width:36px;height:36px;border-radius:50%;display:flex;align-items:center;justify-content:center;font-size:14px;color:var(--brown)}

/* varietals */
.variety{position:absolute;top:2124px;width:282px}
.variety .pic{height:144px}
.variety h3{position:absolute;left:40px;top:160px;font-weight:400;font-size:17px;color:var(--ink)}
.variety p{position:absolute;left:40px;top:188px;width:230px;font-size:12.5px;line-height:17px;color:var(--grey)}
.variety a{position:absolute;left:40px;top:256px;font-size:11px;color:var(--ink);text-decoration:underline}
.variety a.hot{color:var(--yellow)}
.mini-arrow{position:absolute;top:2074px;width:24px;height:24px;border:1.5px solid var(--yellow);border-radius:50%;display:flex;align-items:center;justify-content:center;font-size:10px;color:var(--brown)}

/* footer */
.footer{left:0;top:2538px;width:1200px;height:379px;background:var(--footer);color:var(--white)}
.fcol{position:absolute;top:2600px;width:300px;text-align:center}
.fcol h4{font-weight:500;font-size:15px;margin-top:16px}
.fcol p{font-size:12px;line-height:17px}
.fdiv{position:absolute;top:2600px;width:1px;height:120px;background:#5f646d}
.fnav{left:0;top:2784px;width:1200px;display:flex;justify-content:center;gap:0;font-size:12px}
.fnav span{padding:0 26px}
.fnav .bar{padding:0;color:#ccc}
.fnav .active{color:var(--yellow);text-decoration:underline}
.fline{left:150px;top:2857px;width:920px;height:1px;background:#5f646d}
.copy{left:156px;top:2876px;font-size:11.5px}
.copy b{font-weight:400;color:var(--yellow)}
.social{top:2868px;width:32px;height:32px;border-radius:50%;border:1.5px solid var(--yellow)}
.social.on{background:var(--yellow)}
</style>
</head>
<body>

<header class="abs site-header"></header>
<div class="abs brand-oval"><i class="dot"></i><span>Meadow Lark Honey</span></div>
<nav class="abs nav">
  <a class="active">Home</a><a>About Us</a><a>Products</a><a>Honey Varietals</a><a>Contact Us</a>
</nav>
<div class="btn btn-line quote-btn">Get Free Quote</div>
<svg class="abs cart" width="52" height="52" viewBox="0 0 52 52" aria-label="Cart">
  <path d="M4 12h7l6 22h22l5-16H14" fill="none" stroke="#2b1512" stroke-width="2"/>
  <circle cx="20" cy="40" r="3" fill="none" stroke="#2b1512" stroke-width="2"/>
  <circle cx="36" cy="40" r="3" fill="none" stroke="#2b1512" stroke-width="2"/>
  <circle cx="43" cy="9" r="8" fill="#e3df0b"/>
  <text x="43" y="12" font-size="8" text-anchor="middle" fill="#2b1512" font-family="Jost,sans-serif">02</text>
</svg>

<section class="abs hero" role="img" aria-label="Close-up photograph of honey bees gathering on a hive"></section>
<svg class="abs" style="left:52px;top:290px" width="30" height="50" viewBox="0 0 30 50"><path d="M24 4L6 25l18 21" fill="none" stroke="#fff" stroke-width="3"/></svg>
<svg class="abs" style="left:1118px;top:290px" width="30" height="50" viewBox="0 0 30 50"><path d="M6 4l18 21L6 46" fill="none" stroke="#e3df0b" stroke-width="3"/></svg>
<h1 class="abs display hero-title" style="font-weight:400">Meadow Lark Honey</h1>
<p class="abs hero-sub">We offer free honey bee swarm removal service within<br>30 miles of Maple Ridge.</p>
<div class="btn btn-solid hero-btn">Explore More</div>

<section>
  <h2 class="abs display intro-title" style="font-weight:400">Meadow Lark Honey</h2>
  <p class="abs intro-lead">We produce and sell only pure raw local honey. Raw honey means it has never been flavored, heated, pasteurized, filtered or has additives of any kind.</p>
  <p class="abs intro-text">We sell raw local honey and beeswax candles at our apiary/farm as well as honey at farmers markets and small stores that specialize in locally grown and produced products. Our usual honey varietals include: Big Leaf Maple, Pacific NW Fireweed, Blackberry Blossom, Japanese Knotweed...</p>
  <div class="btn btn-solid intro-btn">Discover More</div>
  <div class="abs intro-art" role="img" aria-label="Jars of golden honey with a wooden dipper, daisies and clover flowers"></div>
</section>

<section>
  <div class="abs band" role="img" aria-label="Blurred wooden beehive boxes in an apiary"></div>
  <div class="abs band-jars" role="img" aria-label="Three dark honey jars with floral labels"></div>
  <form class="abs quote-card">
    <svg class="quote-head" width="358" height="120" viewBox="0 0 358 120"><path d="M0 0h358v105Q179 70 0 105z" fill="#2b1512"/></svg>
    <h2>Request A Quote</h2>
    <p class="lede">Lorem Ipsum has been the industry's standard dummy text ever</p>
    <div class="field" style="top:142px">Name</div>
    <div class="field" style="top:187px">Phone</div>
    <div class="field" style="top:232px">Email</div>
    <div class="field" style="top:277px;height:100px">Message...</div>
    <div class="btn send-btn"><i style="width:10px;height:10px;border-radius:50%;background:#2b1512"></i>Send</div>
  </form>
</section>

<section>
  <div class="abs featured"></div>
  <h2 class="abs display section-title" style="left:156px;top:1482px;font-weight:400">Featured Products</h2>
  <div class="abs title-rule" style="left:460px;top:1506px"></div>
  <div class="btn btn-line viewall" style="left:932px;top:1490px">View All</div>
  <div class="circle-arrow" style="left:96px;top:1726px;border:1.5px solid var(--yellow)">&laquo;</div>
  <div class="circle-arrow" style="left:1066px;top:1726px;background:var(--yellow)">&raquo;</div>

  <article class="product" style="left:156px"><div class="jar" role="img" aria-label="Honey jar"></div><div class="sep"></div><p class="name">Lorem Ipsum available<br>slightly</p><p class="price">$10.00</p><div class="btn btn-line order">Order Now!</div></article>
  <article class="product lift" style="left:383px"><div class="jar" role="img" aria-label="Honey jar"></div>
    <div class="hover-icons">
      <span><svg width="14" height="14" viewBox="0 0 14 14"><circle cx="6" cy="6" r="4" fill="none" stroke="#fff" stroke-width="1.5"/><path d="M9 9l4 4" stroke="#fff" stroke-width="1.5"/></svg></span>
      <span class="on"><svg width="14" height="14" viewBox="0 0 14 14"><path d="M7 12L2 7a2.6 2.6 0 015-3 2.6 2.6 0 015 3z" fill="#2b1512"/></svg></span>
      <span><svg width="14" height="14" viewBox="0 0 14 14"><path d="M2 5h9l-2-2M12 9H3l2 2" fill="none" stroke="#fff" stroke-width="1.5"/></svg></span>
    </div>
    <div class="sep"></div><p class="name">Lorem Ipsum available<br>slightly</p><p class="price">$10.00</p><div class="btn btn-solid order">Order Now!</div></article>
  <article class="product" style="left:613px"><div class="jar" role="img" aria-label="Honey jar"></div><div class="sep"></div><p class="name">Lorem Ipsum available<br>slightly</p><p class="price">$10.00</p><div class="btn btn-line order">Order Now!</div></article>
  <article class="product" style="left:840px"><div class="jar" role="img" aria-label="Honey jar"></div><div class="sep"></div><p class="name">Lorem Ipsum available<br>slightly</p><p class="price">$10.00</p><div class="btn btn-line order">Order Now!</div></article>
</section>

<section>
  <h2 class="abs display section-title" style="left:156px;top:2064px;font-weight:400">Honey Varietals</h2>
  <div class="abs title-rule" style="left:428px;top:2088px"></div>
  <div class="mini-arrow" style="left:985px">&laquo;</div>
  <div class="mini-arrow" style="left:1018px">&raquo;</div>

  <article class="variety" style="left:156px"><div class="pic" role="img" aria-label="Blueberries ripening on a bush" style="background:linear-gradient(135deg,#3f6e2a,#2d4e6e 60%,#4e7c34)"></div>
    <h3>Blueberry</h3><p>Taken from the tiny white flowers of the blueberry bush, the nectar makes a honey that is fruity and luscious...</p><a>Read More</a></article>
  <article class="variety" style="left:460px"><div class="pic" role="img" aria-label="Meadow of pink fireweed below mountains" style="background:linear-gradient(180deg,#9fb7d2 0%,#7d8f8a 35%,#5c7a3a 55%,#b0457e 80%,#6a7a3a)"></div>
    <h3>Fireweed</h3><p>Fireweed honey is very light in color and comes from a summer blooming perennial that is the first plant to...</p><a class="hot">Read More</a></article>
  <article class="variety" style="left:764px"><div class="pic" role="img" aria-label="White blackberry blossoms among leaves" style="background:radial-gradient(circle at 45% 40%,#e9e6e2 0%,#9aa383 30%,#3e5a2a 75%)"></div>
    <h3>Blackberry</h3><p>Blackberry is the number one nectar source for bees in our area. It is very smooth in texture, delightfully...</p><a>Read More</a></article>

  <div class="btn btn-line" style="left:544px;top:2442px;width:112px;height:34px">View All</div>
</section>

<footer class="abs footer"></footer>
<div class="fcol" style="left:150px">
  <svg width="34" height="40" viewBox="0 0 34 40"><path d="M17 38C7 25 4 19 4 14a13 13 0 0126 0c0 5-3 11-13 24z" fill="none" stroke="#e3df0b" stroke-width="2"/><circle cx="17" cy="14" r="4.5" fill="none" stroke="#e3df0b" stroke-width="2"/></svg>
  <h4>Meadow Lark Honey</h4>
  <p>4410 Clover Field Rd,<br>Hollis, WA 98011</p>
</div>
<div class="fdiv" style="left:448px"></div>
<div class="fcol" style="left:450px">
  <svg width="40" height="40" viewBox="0 0 40 40"><path d="M10 5l6 6-4 5c2 5 6 9 11 11l5-4 6 6-5 5C17 34 6 23 5 10z" fill="none" stroke="#e3df0b" stroke-width="2"/></svg>
  <h4 style="font-size:19px;font-weight:400;margin-top:12px">Call: +1 206-555-0148</h4>
  <p>Fax: +1 206-555-0149</p>
</div>
<div class="fdiv" style="left:752px"></div>
<div class="fcol" style="left:754px">
  <svg width="40" height="40" viewBox="0 0 40 40"><circle cx="20" cy="20" r="16" fill="none" stroke="#e3df0b" stroke-width="2"/><circle cx="20" cy="20" r="7" fill="none" stroke="#e3df0b" stroke-width="2"/><path d="M9 9l6 6M31 9l-6 6M9 31l6-6M31 31l-6-6" stroke="#e3df0b" stroke-width="2"/></svg>
  <h4>Need Help?</h4>
  <p><span style="color:var(--yellow);text-decoration:underline">info@meadowlarkhoney.com</span><br>Contact Us</p>
</div>
<nav class="abs fnav">
  <span class="active">Home</span><span class="bar">|</span><span>About Us</span><span class="bar">|</span><span>Products</span><span class="bar">|</span><span>Honey Varietals</span><span class="bar">|</span><span>Contact Us</span>
</nav>
<div class="abs fline"></div>
<p class="abs copy">© 2017 <b>Meadow Lark Honey</b>. All Rights Reserved.</p>
<div class="abs social" style="left:814px"></div>
<div class="abs social on" style="left:854px"></div>
<div class="abs social" style="left:894px"></div>
<div class="abs social" style="left:934px"></div>
<svg class="abs" style="left:1012px;top:2870px" width="14" height="26" viewBox="0 0 14 26"><path d="M7 24V3M2 8l5-5 5 5" fill="none" stroke="#e3df0b" stroke-width="2"/></svg>

</body>
</html>
```